Mortgage Protection Insurance Flyer

The target audience are new home owners so the design needs to be clean and simple.

This a primarily for Final Expense Insurance, but need an area where it says "We Also Specialize In:"
- Medicare Supplement Insurance (MediGap)
- Annuities
- Final Expense

All flyer versions need to be editable. Colors to be used are red, white or black. Refer to my website for colors and photos (brightmeadowcover.com). Will attach my logo and a flyer that I found online that is the format that I am looking for (for 8.5 in. x 11 in version). Need flyer in standard letter size 8.5 in. x11 in. but also in 8.5 in. x 5.5 in and 5.0 in. x 8.0 in. All sizes to be portrait oriented. If picked as winning design, need all flyer versions in full color, also in grey scale and files in all industry file types.

Content can be taken from my website..... brightmeadowcover.com

Do NOT submit if you are not willing to provide all versions as described above for the original project price.

Must use royalty-free stock photos please.

Target Market(s)

New homeowners looking for insurance to protect there mortgage payments

Industry/Entity Type

Life Insurance

Colors
f69fa3

Requirements
Must have
• Colors to be used are red, white or black.
• Need flyer in standard letter size 8.5 in. x11 in. but also in 3.5 in. x 8.5 in (Full Bleed 3.75 in by 8.75 in.) and 4.0 in. x 6.0 in. (Full Bleed 4.12 in x 6.12 in) Each design tailored to the size dimensions (So no squeezing 8.5 x 11 design into a 4.0 x 6.0 space.) All sizes to be portrait oriented. If picked as winning design, need all flyer versions in full color, also in grey scale and files in all file types.
• Do not need physical address on flyer, do need email address on flyer though - tkelvin@brightmeadowcover.com
• So phone number should be prominent, email address and website address should also be contact area.
• If you can not agree to terms above, do not submit any designs.
• Need facebook & twitter logos somewhere in contact info area.
Nice to have
• See sample flyers I have attached.
• White background with red used as primary graphic color and black used as secondary graphic if needed.
• font to be used should similar to one used in logo.

```html
<!DOCTYPE html>
<html lang="en">
<head>
<meta charset="utf-8">
<title>Bright Meadow Cover – Insurance Flyer</title>
<link href="https://fonts.googleapis.com/css2?family=Barlow:ital,wght@0,800;1,700&family=Lato:wght@400;700;900&display=swap" rel="stylesheet">
<style>
  :root {
    --red: #e21f26;
    --red-dark: #8e1118;
    --ink: #1a1a1a;
    --white: #ffffff;
    --panel: #f3f4f6;
  }
  * { box-sizing: border-box; margin: 0; padding: 0; }
  html, body { width: 970px; height: 1200px; overflow: hidden; background: var(--white); }
  .flyer { position: relative; width: 970px; height: 1200px; background: var(--white); font-family: "Lato", sans-serif; color: var(--ink); }
  .graphics { position: absolute; inset: 0; }
  .headline { position: absolute; left: 47px; top: 92px; color: var(--white); font-family: "Barlow", sans-serif; }
  .headline h1 { font-weight: 800; font-size: 25px; line-height: 30px; }
  .headline p { font-style: italic; font-weight: 700; font-size: 18px; line-height: 23px; margin-top: 2px; }
  .brand { position: absolute; left: 586px; top: 84px; display: flex; align-items: center; gap: 10px; }
  .brand-mark { width: 22px; height: 22px; background: var(--red); }
  .brand-name { font-weight: 900; font-size: 26px; letter-spacing: 0.5px; color: var(--ink); }
  .column { position: absolute; top: 700px; }
  .column.mortgage { left: 56px; width: 425px; }
  .column.final { left: 521px; top: 698px; width: 400px; }
  .column h2 { color: var(--red); font-weight: 700; font-size: 18px; margin-bottom: 16px; }
  .column h3 { color: var(--red); font-weight: 700; font-size: 18px; margin: 14px 0 12px; }
  .column p { font-size: 14.6px; line-height: 18.5px; }
  .benefits { list-style: none; }
  .benefits li { position: relative; padding-left: 12px; font-size: 14.6px; line-height: 18.5px; }
  .benefits li::before { content: ""; position: absolute; left: 1px; top: 7px; width: 5px; height: 5px; border-radius: 50%; background: var(--red); }
  .mortgage .benefits li { margin-bottom: 7px; }
  .final h3.specialize { font-size: 16px; margin: 14px 0 6px; }
  .specialties { list-style: none; display: flex; gap: 14px; }
  .specialties li { position: relative; padding-left: 12px; font-size: 14.6px; line-height: 18.5px; font-weight: 700; }
  .specialties li::before { content: ""; position: absolute; left: 1px; top: 7px; width: 5px; height: 5px; border-radius: 50%; background: var(--red); }
  .contact { position: absolute; right: 53px; top: 1108px; text-align: right; color: var(--white); font-weight: 700; }
  .contact .phone-row { display: flex; justify-content: flex-end; align-items: center; gap: 10px; }
  .contact .phone { font-size: 26px; font-weight: 900; line-height: 32px; }
  .social { width: 22px; height: 22px; border-radius: 50%; background: var(--white); }
  .contact .web { font-size: 17px; line-height: 26px; margin-top: 4px; }
</style>
</head>
<body>
<div class="flyer">
  <svg class="graphics" width="970" height="1200" viewBox="0 0 970 1200">
    <defs>
      <linearGradient id="redBand" x1="0" y1="0" x2="1" y2="0">
        <stop offset="0" stop-color="#8e1118"/>
        <stop offset="1" stop-color="#e21f26"/>
      </linearGradient>
      <linearGradient id="photoTone" x1="0" y1="0" x2="1" y2="0.3">
        <stop offset="0" stop-color="#cdbfbe"/>
        <stop offset="0.45" stop-color="#4a4244"/>
        <stop offset="1" stop-color="#2e2a2c"/>
      </linearGradient>
      <radialGradient id="couplePhoto" cx="0.5" cy="0.45" r="0.6">
        <stop offset="0" stop-color="#e3c3a8"/>
        <stop offset="1" stop-color="#9fb3c3"/>
      </radialGradient>
    </defs>
    <rect x="484" y="645" width="486" height="470" fill="var(--panel)"/>
    <path role="img" aria-label="Photo: businessman holding a paper umbrella over a paper cut-out family, house and car"
          d="M0,290 C180,300 360,200 600,175 C760,165 880,170 970,180 L970,543 C800,620 560,660 330,650 C220,640 120,560 0,458 Z"
          fill="url(#photoTone)"/>
    <path d="M0,0 L300,0 C420,40 520,110 593,161 C430,200 280,300 120,290 C70,286 30,280 0,272 Z" fill="url(#redBand)"/>
    <path d="M0,272 C30,280 70,286 120,290 C280,300 430,200 593,161 C430,215 280,318 120,310 C70,307 30,300 0,292 Z" fill="var(--white)"/>
    <circle cx="188" cy="526" r="160" fill="var(--white)"/>
    <circle role="img" aria-label="Photo: smiling senior couple embracing" cx="188" cy="526" r="153" fill="url(#couplePhoto)"/>
    <path d="M0,1200 L0,1195 C300,1150 600,1060 970,1068 L970,1200 Z" fill="url(#redBand)"/>
  </svg>

  <div class="headline">
    <h1>OUR PLANS ARE BASED ON YOURS</h1>
    <p>Get the right Final Expense Insurance,<br>Medicare Supplement Insurance or<br>Mortgage Protection Insurance plan<br>for your family's peace-of-mind!</p>
  </div>

  <div class="brand">
    <span class="brand-mark"></span>
    <span class="brand-name">BRIGHT MEADOW COVER</span>
  </div>

  <section class="column mortgage">
    <h2>MORTGAGE PROTECTION INSURANCE</h2>
    <p>Mortgage Protection Insurance (MPI) is a type of decreasing term life insurance policy designed to pay off your mortgage if you were to pass away — and many policies also cover mortgage payments (usually for a limited period of time) if you become disabled.</p>
    <h3>BENEFITS:</h3>
    <ul class="benefits">
      <li>Guaranteed approval. Even if you're in poor health or work in a dangerous profession, there is guaranteed approval with no medical exams or lab tests.</li>
      <li>No guesswork. The check goes straight to the lender for the exact mortgage balance, so there'll always be enough and your family won't have to handle the money.</li>
      <li>Disability protection. Many MPI policies make mortgage payments (usually for a limited time) if you become disabled or lose your job.</li>
    </ul>
  </section>

  <section class="column final">
    <h2>FINAL EXPENSE INSURANCE</h2>
    <p>Final Expense Insurance is a type of permanent life insurance where the death benefit is used to cover (but not limited to) medical costs, funeral costs and other end-of-life expenses. It is a budget friendly option with a death benefit of up to $35k.</p>
    <h3>BENEFITS:</h3>
    <ul class="benefits">
      <li>Relatively low monthly premiums</li>
      <li>Premiums can never increase</li>
      <li>Your policy can never be cancelled as long as you pay your premium</li>
      <li>No medical exams</li>
      <li>Guaranteed Death Benefit</li>
      <li>Many policies are Guaranteed Acceptance</li>
    </ul>
    <h3 class="specialize">WE ALSO SPECIALIZE IN:</h3>
    <ul class="specialties">
      <li>MediGap</li>
      <li>Annuities</li>
      <li>Final Expense</li>
    </ul>
  </section>

  <div class="contact">
    <div class="phone-row">
      <span class="social" role="img" aria-label="Social profile"></span>
      <span class="social" role="img" aria-label="Social profile"></span>
      <span class="phone">(555)014.2237</span>
    </div>
    <div class="web">tkelvin@brightmeadowcover.com | www.brightmeadowcover.com</div>
  </div>
</div>
</body>
</html>
```